I need a business card design for a new company that will be doing consulting work around issues of cultural competency, and diversity and inclusion. I would like the design to be crisp and clear with bold but conservative colors and incorporate shades of blue

Target Market(s)

Small businesses, schools, non-profits

Industry/Entity Type

Consulting

Font styles to use
Serif
Sans Serif

Colors
0c5ba6
6b449b
3276b5
0292cd

Requirements
Must have
• A Morrow Venture (name of company)
• Tiru Morrow
• CEO
• tiru@amorrowventure.example
• (215)555-0147

```html
<!DOCTYPE html>
<html lang="en">
<head>
<meta charset="utf-8">
<title>A Morrow Venture – Business Card</title>
<link rel="stylesheet" href="https://fonts.googleapis.com/css2?family=Lora:wght@400;700&display=swap">
<style>
  :root {
    --brand-blue: #125ea8;
    --brand-purple: #6b449b;
    --ribbon-fold: #9a80c0;
    --paper: #ffffff;
    --paper-texture: #f3f6fb;
    --reflection: #c3cedb;
    --stage: #ece7df;
    --ink-light: #ffffff;
  }
  * { margin: 0; padding: 0; box-sizing: border-box; }
  html, body {
    width: 1200px; height: 1200px; overflow: hidden;
    background: var(--stage);
    font-family: "Lora", Georgia, serif;
  }
  .business-card {
    position: absolute; left: 100px; top: 314px;
    width: 1000px; height: 572px;
    background: var(--paper);
    box-shadow: 0 10px 30px rgba(0,0,0,0.18);
    overflow: hidden;
  }
  .card-upper {
    position: absolute; left: 0; top: 0; width: 1000px; height: 343px;
    background: var(--paper-texture);
  }
  .company-name,
  .company-name-reflection {
    position: absolute; left: 0; right: 0; height: 56px;
    text-align: center;
    font-weight: 700; font-size: 56px; letter-spacing: 5px; line-height: 56px;
    text-transform: uppercase; white-space: nowrap;
  }
  .company-name {
    top: 120px; color: var(--brand-blue); z-index: 2;
  }
  /* mirrored below the baseline: flip about the baseline, then push down a few px */
  .company-name-reflection {
    top: 124px; color: var(--reflection);
    transform-origin: 0 48px;
    transform: scaleY(-0.28);
    opacity: 0.75;
    z-index: 1;
  }
  .card-band {
    position: absolute; left: 0; top: 343px; width: 1000px; height: 229px;
    background: var(--brand-blue);
  }
  .name-ribbon {
    position: absolute; left: 0; top: 0; width: 1000px; height: 572px;
  }
  .holder {
    position: absolute; left: 0; right: 0; top: 333px;
    text-align: center; color: var(--ink-light);
  }
  .holder-name {
    font-size: 33px; letter-spacing: 1.5px; line-height: 1; text-transform: uppercase;
  }
  .holder-name strong { font-weight: 700; }
  .holder-role {
    margin-top: 12px; font-size: 21px; letter-spacing: 4px; line-height: 1;
  }
  .contact {
    position: absolute; top: 478px; display: flex; align-items: center;
    color: var(--ink-light); font-size: 23px; letter-spacing: 3px; line-height: 1;
  }
  .contact-phone { left: 36px; gap: 18px; }
  .contact-email { right: 36px; gap: 22px; letter-spacing: 2px; }
  .contact svg { display: block; }
</style>
</head>
<body>
  <div class="business-card">
    <div class="card-upper" role="img" aria-label="Fine diagonal line texture in pale blue"></div>
    <div class="company-name-reflection" aria-hidden="true">A Morrow Venture</div>
    <h1 class="company-name">A Morrow Venture</h1>
    <div class="card-band"></div>

    <svg class="name-ribbon" viewBox="0 0 1000 572" aria-hidden="true">
      <polygon points="233,343 250,318 258,343" fill="var(--ribbon-fold)"/>
      <polygon points="767,343 750,318 742,343" fill="var(--ribbon-fold)"/>
      <polygon points="250,318 750,318 707,418 290,418" fill="var(--brand-purple)"/>
    </svg>

    <div class="holder">
      <p class="holder-name"><strong>Tiru</strong> Morrow</p>
      <p class="holder-role">CEO</p>
    </div>

    <div class="contact contact-phone">
      <svg width="34" height="28" viewBox="0 0 34 28" aria-hidden="true">
        <path d="M2 9 C2 3 32 3 32 9 L32 12 L24 12 L24 8 L10 8 L10 12 L2 12 Z" fill="#fff"/>
        <path d="M8 13 L12 10 L22 10 L26 13 L30 26 L4 26 Z" fill="#fff"/>
        <circle cx="17" cy="18" r="4" fill="var(--brand-blue)"/>
      </svg>
      <span>(215)555-0147</span>
    </div>

    <div class="contact contact-email">
      <span>tiru@amorrowventure.example</span>
      <svg width="34" height="26" viewBox="0 0 34 26" aria-hidden="true">
        <rect x="1" y="1" width="32" height="24" fill="#fff"/>
        <polyline points="2,2 17,15 32,2" fill="none" stroke="var(--brand-blue)" stroke-width="1.6"/>
        <line x1="2" y1="24" x2="13" y2="12" stroke="var(--brand-blue)" stroke-width="1.2"/>
        <line x1="32" y1="24" x2="21" y2="12" stroke="var(--brand-blue)" stroke-width="1.2"/>
      </svg>
    </div>
  </div>
</body>
</html>
```